Business Card Design - Corporate

Create a sleek elegant business card layout while suggesting a color scheme. Convey cutting edge technology while maintaining a corporate feel that is easily readable.

Company designs and manufactures consumer electronic products for mass retail that are mainly app driven.

(vector logo and die-line provided)

Target Market(s)

Corporate level, tech industry.

Industry/Entity Type

Business

Contact Information for Business Card

Generic Info:

Name
Title
email
address
phone 1
phone 2
website (quillbarn.com) on back

Font styles to use
Sans Serif

Requirements
Must have
• At least 2 colors + white on one side.
Nice to have
• Solid suggestion on color for logo and overall design. Color flood on back of card.
Should not have
• background texture like... marble, stone, patterns or circuit boards

```html
<!DOCTYPE html>
<html lang="en">
<head>
<meta charset="utf-8">
<title>Quillbarn Business Card</title>
<link rel="stylesheet" href="https://fonts.googleapis.com/css2?family=Ubuntu:wght@400;500&display=swap">
<style>
  :root {
    --brand-blue: #0a6bc4;
    --ink-grey: #4a4a4c;
    --text-grey: #555558;
    --paper: #ffffff;
    --backdrop: #e3e4e6;
  }
  * { margin: 0; padding: 0; box-sizing: border-box; }
  html, body { width: 1200px; height: 1200px; overflow: hidden; }
  body {
    background: var(--backdrop);
    font-family: "Ubuntu", sans-serif;
    position: relative;
  }
  .card {
    position: absolute;
    left: 150px;
    width: 900px;
    height: 514px;
    background: var(--paper);
    box-shadow: 0 6px 18px rgba(0,0,0,0.12);
    overflow: hidden;
  }
  .card--front { top: 50px; }
  .card--back { top: 630px; }

  .wordmark {
    position: absolute;
    display: flex;
    align-items: center;
    gap: 14px;
    color: var(--ink-grey);
    font-weight: 400;
    letter-spacing: 0.16em;
    white-space: nowrap;
  }
  .wordmark__dot {
    width: 0.6em; height: 0.6em;
    border-radius: 50%;
    background: var(--brand-blue);
  }
  .card--front .wordmark { right: 70px; top: 70px; font-size: 54px; }
  .card--back .wordmark { left: 0; right: 0; top: 150px; justify-content: center; font-size: 72px; }

  .stripe { position: absolute; left: 0; right: 0; }
  .stripe__rule { position: absolute; left: 0; right: 0; height: 3px; background: var(--brand-blue); top: 0; }
  .stripe__band { position: absolute; left: 0; right: 0; height: 38px; background: var(--brand-blue); top: 10px; }
  .stripe__edge { position: absolute; left: 0; right: 0; height: 4px; background: var(--brand-blue); top: 54px; }
  .card .stripe { bottom: 0; height: 58px; }

  .holder {
    position: absolute;
    left: 60px;
    top: 190px;
    color: var(--text-grey);
    font-size: 22px;
    line-height: 1.45;
  }
  .holder__name {
    color: var(--brand-blue);
    font-weight: 500;
    font-size: 34px;
    letter-spacing: 0.02em;
    line-height: 1.2;
  }

  .contacts {
    position: absolute;
    right: 70px;
    top: 250px;
    width: 370px;
    display: flex;
    flex-direction: column;
    gap: 14px;
    font-size: 21px;
    color: var(--text-grey);
  }
  .contacts__group {
    border-left: 2px solid var(--brand-blue);
    padding-left: 22px;
    line-height: 1.5;
  }
  .contacts__label { color: var(--brand-blue); font-weight: 500; display: inline-block; width: 34px; }
</style>
</head>
<body>
  <section class="card card--front" aria-label="Business card front">
    <div class="wordmark"><span>QUILLBARN</span><span class="wordmark__dot"></span></div>
    <div class="holder">
      <div class="holder__name">JOHN DOE</div>
      <div>Director</div>
      <div>Dummy city</div>
      <div>Dummy country land</div>
    </div>
    <div class="contacts">
      <div class="contacts__group">
        <div><span class="contacts__label">T :</span>123-456-7890</div>
        <div><span class="contacts__label">F :</span>123-456-7890</div>
      </div>
      <div class="contacts__group">
        <div><span class="contacts__label">W :</span>www.quillbarn.com</div>
        <div><span class="contacts__label">E :</span>john@quillbarn.com</div>
      </div>
    </div>
    <div class="stripe">
      <div class="stripe__rule"></div>
      <div class="stripe__band"></div>
      <div class="stripe__edge"></div>
    </div>
  </section>

  <section class="card card--back" aria-label="Business card back">
    <div class="wordmark"><span>QUILLBARN</span><span class="wordmark__dot"></span></div>
    <div class="stripe">
      <div class="stripe__rule"></div>
      <div class="stripe__band"></div>
      <div class="stripe__edge"></div>
    </div>
  </section>
</body>
</html>
```